Printing company needs a presentational catalogue, min. A5 format when closed, portrait or landscape

We need a corporate catalogue design for presentation of our company/services mainly to corporate customers. Our portfolio of services includes: offset printing, digital printing, screen printing, UV flatbed printing, direct UV printing on promotional items, textile printing (direct screen printing and heat transfer), computer cutting/plotting, CNC cutting, graphic design, setting for press; You can also use images of our products from our website www.lastovkabarve.si
We will adopt text later to the design so there should be some free space left for text. You should also determinate the typography of fonts for the category titles (offset printing, digital printing, etc...) and description of individual category.
Design should communicate in a way that we are there to solve our customer´s graphic problems and needs. Our new logo is attached. Catalogue colours should be matched with our new logo (kobalt lini). We will change our website soon (from lastovkabarve to kobaltlini), so the catalogue should not be in colours of existent website design (blue and orange).

Target Market(s)

B2B customers (mixed field of work)

Industry/Entity Type

Printing

Requirements
Must have
• Our new company logo, but it should not step out too much (better to be small and discreet).
Nice to have
• Some images of products that we offer - they could be from our website www.lastovkabarve.si if you can integrate them well into design...

```html
<!DOCTYPE html>
<html lang="en">
<head>
<meta charset="utf-8">
<title>Kobalt Lini – Catalogue</title>
<link href="https://fonts.googleapis.com/css2?family=Ubuntu:wght@500;700&family=Open+Sans:wght@400;600&family=Great+Vibes&display=swap" rel="stylesheet">
<style>
  :root{
    --bg:#ececec;
    --panel:#d9e3ec;
    --panel-top:#e8eef3;
    --grey:#e4e5e6;
    --ink:#2b2b2b;
    --orange:#f3a12b;
    --red:#d3202f;
    --teal:#3aae9f;
    --blue:#1f78c1;
    --deep-teal:#2c7b6f;
    --white:#ffffff;
  }
  *{margin:0;padding:0;box-sizing:border-box}
  html,body{width:1200px;height:800px;overflow:hidden;background:var(--bg)}
  body{font-family:"Open Sans",sans-serif;color:var(--ink)}
  .strip{position:absolute;left:40px;display:flex;width:1120px;height:280px;box-shadow:0 2px 6px rgba(0,0,0,.12)}
  .strip--outer{top:90px}
  .strip--inner{top:430px}
  .panel{position:relative;width:280px;height:280px;overflow:hidden;background:var(--panel)}
  .panel::before{content:"";position:absolute;left:0;top:0;width:100%;height:14px;background:var(--panel-top)}
  .section-bar{position:absolute;left:0;top:14px;width:100%;height:32px;display:flex;align-items:center;padding-left:14px;
    font-family:"Ubuntu",sans-serif;font-weight:700;font-size:15px;color:var(--white);z-index:3}
  .section-lead{position:absolute;left:14px;top:52px;font-family:"Ubuntu",sans-serif;font-weight:700;font-size:13px;white-space:nowrap;z-index:3}
  .section-copy{position:absolute;left:14px;top:70px;width:250px;font-size:5.6px;line-height:1.45;color:#333;z-index:2}
  .section-copy--narrow{width:128px}
  .product-photo{position:absolute;left:0;right:0;bottom:0}
  .cnc .section-bar{background:var(--orange)} .cnc .section-lead{color:var(--orange)}
  .offset .section-bar{background:var(--red)} .offset .section-lead{color:var(--red)}
  .digital .section-bar{background:var(--teal)} .digital .section-lead{color:var(--teal)}
  .screen .section-bar{background:var(--blue)} .screen .section-lead{color:var(--blue)}
  .uv .section-bar{background:var(--deep-teal)} .uv .section-lead{color:var(--deep-teal)}

  .back-cover{background:var(--grey)}
  .back-cover::before{display:none}
  .contact{position:absolute;left:0;right:0;top:140px;text-align:center}
  .brand{display:inline-flex;align-items:center;gap:6px;font-family:"Ubuntu",sans-serif;font-weight:500;font-size:13px;letter-spacing:.5px;color:#1d1d1d;text-transform:uppercase}
  .brand-mark{width:14px;height:14px;background:var(--red);border-radius:2px}
  .contact-lines{margin-top:5px;font-size:5.6px;line-height:1.5;color:#333}
  .web-band{position:absolute;left:0;right:0;top:228px;height:32px;background:var(--white);display:flex;align-items:center;justify-content:center;
    font-weight:600;font-size:12px;color:#1d1d1d}

  .front-cover .product-photo{top:0}
  .front-cover .brand-band{position:absolute;left:0;right:0;top:228px;height:32px;background:var(--white);display:flex;align-items:center;justify-content:center}

  .welcome .product-photo{top:0;opacity:.35}
  .welcome::before{display:none}
  .welcome-frame{position:absolute;left:58px;width:210px;height:12px;background:var(--red)}
  .welcome-frame--top{top:3px}
  .welcome-frame--bottom{top:265px}
  .welcome-title{position:absolute;left:58px;width:210px;top:72px;text-align:center;font-family:"Great Vibes",cursive;font-size:30px;color:var(--red);line-height:1}
  .welcome-sub{position:absolute;left:58px;width:210px;top:102px;text-align:center;font-size:11px;color:#222}
  .welcome-copy{position:absolute;left:62px;width:200px;top:120px;font-size:5.6px;line-height:1.5;text-align:justify;color:#222}
</style>
</head>
<body>

<section class="strip strip--outer">
  <article class="panel cnc">
    <div class="section-bar">CNC Cutting</div>
    <h3 class="section-lead">Lorem Ipsum is simply</h3>
    <p class="section-copy">of the printing and typesetting industry. Lorem Ipsum has been the industry's standard dummy text ever since the 1500s, when an unknown printer took a galley of type and scrambled it to make a type specimen book. It has survived not only five centuries, but also the leap into electronic typesetting, remaining essentially unchanged. It was popularised in the 1960s with the release of Typesheet sheets containing Lorem Ipsum passages, and more.</p>
    <div class="product-photo" style="top:120px;background:linear-gradient(135deg,#7d9bb8 0%,#c9d3dc 35%,#b8322e 60%,#8f8a86 80%,#e6e1dc 100%)" role="img" aria-label="CNC cut foam letters, cut-out sheets and branded drink cups"></div>
  </article>

  <article class="panel back-cover">
    <div class="contact">
      <div class="brand"><span class="brand-mark"></span>Kobalt Lini</div>
      <div class="contact-lines">
        Lipova cesta 12<br>
        1000 Ljubljana - Bežigrad<br>
        Tel: 01 555 12 34 / Gsm: 041 555 678<br>
        E-pošta: info@kobaltlini.si<br>
        ID št. za DDV: SI12345678<br>
        TRR: SI56 0000 0000 1111 222 Banka d.d.
      </div>
    </div>
    <div class="web-band">www.kobaltlini.si</div>
  </article>

  <article class="panel front-cover">
    <div class="product-photo" style="background:linear-gradient(160deg,#e2b640 0%,#3d9a4c 28%,#c8862e 45%,#6b3b22 62%,#23262c 80%,#8b98a6 100%)" role="img" aria-label="Collage of printed products: labels, bottle, lanyards, label rolls, t-shirt and packaging"></div>
    <div class="brand-band"><div class="brand"><span class="brand-mark"></span>Kobalt Lini</div></div>
  </article>

  <article class="panel welcome">
    <div class="product-photo" style="background:linear-gradient(160deg,#e2b640 0%,#3d9a4c 30%,#c8862e 50%,#6b3b22 70%,#8b98a6 100%)" role="img" aria-label="Faded collage of printed products"></div>
    <div class="welcome-frame welcome-frame--top"></div>
    <h2 class="welcome-title">Welcome</h2>
    <p class="welcome-sub">to Kobalt Lini</p>
    <p class="welcome-copy">of the printing and typesetting industry. Lorem Ipsum has been the industry's standard dummy text ever since the 1500s, when an unknown printer took a galley of type and scrambled it to make a type specimen book. It has survived not only five centuries, but also the leap into electronic typesetting, remaining essentially unchanged. It was popularised in the 1960s with the release of Typesheet sheets. Lorem Ipsum is simply dummy text of the printing and typesetting industry. Lorem Ipsum has been the industry's standard dummy text ever since the 1500s, when an unknown printer took a galley of type and scrambled it to make a type specimen book. It has survived not only five centuries, but also the leap into electronic typesetting, remaining essentially unchanged. It was popularised in the 1960s with the release of Typesheet sheets.</p>
    <div class="welcome-frame welcome-frame--bottom"></div>
  </article>
</section>

<section class="strip strip--inner">
  <article class="panel offset">
    <div class="section-bar">Offset Printing</div>
    <h3 class="section-lead">Lorem Ipsum is simply</h3>
    <p class="section-copy">of the printing and typesetting industry. Lorem Ipsum has been the industry's standard dummy text ever since the 1500s, when an unknown printer took a galley of type and scrambled it to make a type specimen book. It has survived not only five centuries, but also the leap into electronic typesetting, remaining essentially unchanged.</p>
    <p class="section-copy section-copy--narrow" style="top:112px">It was popularised in the 1960s with the release of Typesheet sheets containing Lorem Ipsum passages, and more recently with desktop publishing software like Folio Layout including versions of Lorem Ipsum.</p>
    <div class="product-photo" style="top:105px;background:linear-gradient(150deg,#dfe7ef 0%,#e9edf2 40%,#c9a24a 65%,#7a3a2a 82%,#2b2b2b 100%)" role="img" aria-label="Offset printed brochures, business cards, catalogues and envelopes"></div>
  </article>

  <article class="panel digital">
    <div class="section-bar">Digital Printing</div>
    <h3 class="section-lead">Lorem Ipsum is simply</h3>
    <p class="section-copy section-copy--narrow">of the printing and typesetting industry. Lorem Ipsum has been the industry's standard dummy text ever since the 1500s, when an unknown printer took a galley of type and scrambled it to make a type it was popularised in the 1960s with the release of Typesheet sheets containing Lorem Ipsum passages, and more recently with desktop publishing software like Folio Layout including versions of Lorem Ipsum.</p>
    <div class="product-photo" style="top:74px;left:150px;background:linear-gradient(160deg,#e3e9ef 0%,#c7d1da 40%,#e1c23a 60%,#2d3238 75%,#d35a4a 100%)" role="img" aria-label="Digitally printed stickers, warning tape and signage"></div>
    <div class="product-photo" style="top:170px;right:130px;background:linear-gradient(120deg,#d7a35a 0%,#e7dfd2 50%,#d5dde4 100%)" role="img" aria-label="Printed sticker sheets"></div>
  </article>

  <article class="panel screen">
    <div class="section-bar">Screen Printing</div>
    <h3 class="section-lead">Lorem Ipsum is simply</h3>
    <p class="section-copy">of the printing and typesetting industry. Lorem Ipsum has been the industry's standard dummy text ever since the 1500s, when an unknown printer took a galley of type and scrambled it to make a type specimen book. It has survived not only five centuries, but also the leap into electronic typesetting, remaining essentially unchanged. It was popularised in the 1960s with the release of Typesheet sheets containing Lorem Ipsum passages, and more recently with desktop publishing software like Folio Layout.</p>
    <div class="product-photo" style="top:120px;background:linear-gradient(160deg,#e4572e 0%,#1e2128 35%,#e9e6df 55%,#2b4a8a 78%,#1c2a4a 100%)" role="img" aria-label="Screen printed t-shirts, bags and textiles"></div>
  </article>

  <article class="panel uv">
    <div class="section-bar">UV Printing</div>
    <h3 class="section-lead">Lorem Ipsum is simply</h3>
    <p class="section-copy section-copy--narrow">of the printing and typesetting industry. Lorem Ipsum has been the industry's standard dummy text ever since the 1500s, when an unknown printer took a galley of type and scrambled it to make a type specimen book. It has survived not only five centuries, but also the leap into electronic typesetting with the release of Typesheet sheets containing Lorem Ipsum passages, and more recently with desktop publishing software like Folio Layout.</p>
    <div class="product-photo" style="top:80px;left:150px;background:linear-gradient(160deg,#b8322e 0%,#7a3a22 35%,#e5d3a8 55%,#c9d3dc 75%,#2e5f9a 100%)" role="img" aria-label="UV printed label rolls, packaging and boxes"></div>
    <div class="product-photo" style="top:185px;right:130px;background:linear-gradient(140deg,#2f5a4e 0%,#3f6e60 60%,#e6e4dc 100%)" role="img" aria-label="UV printed folder with embossed seal"></div>
  </article>
</section>

</body>
</html>
```